Business Card Design

We need a business card designed to the point of print ready to take to our printers. the design should be professional, easy to read and simple. The cards should represent our business as professional and trust worthy.

Attached are several versions o the logo, and also the details for the card to be printed. please do communicate if different versions of the logo is required.

Business

```html
<!DOCTYPE html>
<html lang="en">
<head>
<meta charset="utf-8">
<title>PayBackPoint Business Cards</title>
<link href="https://fonts.googleapis.com/css2?family=Source+Sans+3:wght@400;600;700&display=swap" rel="stylesheet">
<style>
  :root {
    --backdrop: #6e625a;
    --orange: #f7a020;
    --white: #ffffff;
    --ink: #1a1a1a;
    --brand-grey: #5f6166;
  }
  * { box-sizing: border-box; margin: 0; padding: 0; }
  html, body { width: 1200px; height: 618px; overflow: hidden; }
  body {
    background: var(--backdrop);
    font-family: "Source Sans 3", Arial, sans-serif;
    position: relative;
  }
  .card {
    position: absolute;
    width: 370px;
    height: 228px;
    box-shadow: 0 6px 14px rgba(0,0,0,0.35);
    overflow: hidden;
  }
  .card--front { background: var(--orange); }
  .card--back { background: var(--white); }

  .pos-left-front { left: 150px; top: 58px; }
  .pos-left-back { left: 150px; top: 326px; }
  .pos-right-front { left: 690px; top: 58px; }
  .pos-right-back { left: 690px; top: 326px; }

  /* front */
  .url-strip {
    position: absolute;
    left: 30px; top: 0; bottom: 0;
    width: 44px;
    background: var(--white);
    display: flex; align-items: center; justify-content: center;
  }
  .url-strip span {
    writing-mode: vertical-rl;
    transform: rotate(180deg);
    font-size: 17px;
    color: var(--ink);
    letter-spacing: 0.2px;
  }
  .brand {
    position: absolute;
    right: 26px; top: 90px;
    color: var(--brand-grey);
    font-weight: 700;
    text-align: right;
    line-height: 1;
  }
  .brand__name { display: block; font-size: 36px; letter-spacing: -0.5px; }
  .brand__suffix { display: block; font-size: 15px; margin-top: 2px; }

  /* back */
  .brand-strip {
    position: absolute;
    right: 22px; top: 0; bottom: 0;
    width: 38px;
    background: var(--orange);
    display: flex; justify-content: center; padding-top: 10px;
  }
  .brand-strip span {
    writing-mode: vertical-rl;
    color: var(--brand-grey);
    font-weight: 700;
    font-size: 22px;
    line-height: 1;
  }
  .person {
    position: absolute;
    left: 26px; top: 30px;
  }
  .person__name { font-size: 21px; color: var(--ink); font-weight: 400; }
  .person__first { color: var(--orange); }
  .person__title { font-size: 14px; color: var(--ink); margin-top: 4px; }
  .contact {
    position: absolute;
    left: 26px; bottom: 12px;
    list-style: none;
    font-size: 14px;
    line-height: 1.4;
    color: var(--ink);
  }
  .contact__label { color: var(--orange); }
</style>
</head>
<body>

  <section class="card card--front pos-left-front">
    <div class="url-strip"><span>www.paybackpoint.com.au</span></div>
    <div class="brand"><span class="brand__name">PayBackPoint</span><span class="brand__suffix">Pty Ltd</span></div>
  </section>

  <section class="card card--back pos-left-back">
    <div class="person">
      <h2 class="person__name"><span class="person__first">Renee</span> Calder</h2>
      <p class="person__title">Managing Director</p>
    </div>
    <ul class="contact">
      <li><span class="contact__label">Phone:</span> +61 400 555 112</li>
      <li><span class="contact__label">Email:</span> rcalder@paybackpoint.com.au</li>
      <li><span class="contact__label">Address:</span> PO Box 1200 Harbour Centre Qld 4000</li>
      <li><span class="contact__label">Web:</span> www.paybackpoint.com.au</li>
    </ul>
    <div class="brand-strip"><span>PayBackPoint Pty Ltd</span></div>
  </section>

  <section class="card card--front pos-right-front">
    <div class="url-strip"><span>www.paybackpoint.com.au</span></div>
    <div class="brand"><span class="brand__name">PayBackPoint</span><span class="brand__suffix">Pty Ltd</span></div>
  </section>

  <section class="card card--back pos-right-back">
    <div class="person">
      <h2 class="person__name"><span class="person__first">Joel</span> Martin</h2>
      <p class="person__title">Director</p>
    </div>
    <ul class="contact">
      <li><span class="contact__label">Phone:</span> +61 400 555 348</li>
      <li><span class="contact__label">Email:</span> jmartin@paybackpoint.com.au</li>
      <li><span class="contact__label">Address:</span> PO Box 1200 Harbour Centre Qld 4000</li>
      <li><span class="contact__label">Web:</span> www.paybackpoint.com.au</li>
    </ul>
    <div class="brand-strip"><span>PayBackPoint Pty Ltd</span></div>
  </section>

</body>
</html>
```